WordPress website in children books redesign

We are personalised children storybook creators with a range of personalized books, music CDs and DVDs that are created for each child. We sell our concept through a license via distributors / entrepreneurs mainly based in France and Europe. We want to focus on selling B2C to parents and grandparents, looking to buy presents to their children aged 0 to 10 years old. Those present are educative, unique for each child, and they will learn to have fun and learn to have fun. I would like to redesign our WordPress website https://pebblelanternkids.co.uk/index.php We are a children in the world of books and music books: books, music CDs and DVDs looking for something a little more along the lines of our competitors. See ike www.quillotop.com, www.tavirosa.com, www.lecheminduvelours.com, https://www.lespetitsbrume.com/, https://tinselpaths.com/ Our current website is a bit too old fashioned so I am looking at a much more modern design Here is a link for a few products that are not available here: https://www.filecrate.example/sh/kq417dzopfrnwtb/BXPL3rYmOk2u-sVH4dQkLN-zb?dl=0 We have 2 sides in our website: B2C on the left side and B2B on the right site; B2B is for distributors that are entrepreneurs buying our concept. for the homepage design, the main focus will be B2Consumer Our current page is too blended, lacks reassurance elements and I would like to have a look at this page. from our current stories. here is a link for our business book to give you a feel for it: http://online.pagewavo.com/qtlk/pzme/ MAIN PAGES TO REVIEW / HOMEPAGE / https://pebblelanternkids.co.uk/ BOOKS: https : //pebblelanternkids.co.uk/product-category/personalised-books/ MUSIC: https://pebblelanternkids.co.uk/product-category/music-cds/ BLOG: https://pebblelanternkids.co.uk/blog -2 / Looking forward to seeing you and your questions asap

Target Market(s)

parents and grandparents of children aged 0 to 10 years old. This is for the European market

Industry/Entity Type

Publishing Company

Number of Pages Required

4 page

Colors
0392cd
9bcb3b
ec1f27
757575

Requirements
Must have
• keep within the color code of our RGB logo: D25028 RGB: 8CC364 329BC8 808285
Nice to have
• be more with the style of our competitors. Pebble Lantern Kids am about making children learn the fun way, and develop their morality, self-esteem and confidence. It's about the magic of reading to help children learn while having fun. I have attached visuals but those are just examples and you we encourage you to suggest other ideas

```html
<!DOCTYPE html>
<html lang="en">
<head>
<meta charset="utf-8">
<title>Pebble Lantern Kids — Personalised Books, Music CDs and DVDs</title>
<link href="https://fonts.googleapis.com/css2?family=Dosis:wght@400;500;600;700&family=Open+Sans:wght@400;600&display=swap" rel="stylesheet">
<style>
:root{
  --orange:#d25028;
  --green:#8cc364;
  --blue:#329bc8;
  --grey:#808285;
  --ink:#222;
  --price:#3a8fc4;
  --purple:#a394e0;
  --pink:#de70bb;
  --footer:#8e9c7a;
  --line:#d9d9d9;
  --white:#fff;
}
*{box-sizing:border-box;margin:0;padding:0}
html,body{width:1200px;height:3516px;overflow:hidden;background:var(--white)}
body{font-family:"Dosis",sans-serif;color:var(--ink);position:relative}
.abs{position:absolute}
a{color:inherit;text-decoration:none}

/* header */
.topbar{left:0;top:0;width:1200px;height:98px;background:var(--white)}
.social{display:flex;gap:12px}
.social span{width:32px;height:32px;border-radius:50%;background:#c5c7c9;display:block}
.social .on{background:var(--blue)}
.pill{border-radius:22px;background:#e8e8e8;font:600 15px "Dosis",sans-serif;display:flex;align-items:center;justify-content:center;gap:10px;color:#333;text-transform:uppercase}
.navbar{left:0;top:98px;width:1200px;height:52px;background:var(--blue)}
.nav{left:272px;top:98px;height:52px;display:flex}
.nav a{height:52px;line-height:52px;padding:0 22px;color:var(--white);font:700 15px "Dosis",sans-serif;text-transform:uppercase}
.nav a.active{background:#1f7eaa}
.search{left:797px;top:105px;width:314px;height:38px;border-radius:20px;background:#2585b3;color:#cfe7f3;font:400 14px "Open Sans",sans-serif;padding:0 22px;display:flex;align-items:center;justify-content:space-between}
.logo{left:82px;top:0;width:126px;height:126px;border-radius:50%;background:var(--white);border:3px solid #eee;display:flex;align-items:center;justify-content:center;text-align:center;font:700 20px/1.05 "Dosis",sans-serif;color:var(--orange);z-index:3}

/* hero */
.hero{left:0;top:150px;width:1200px;height:440px;background:linear-gradient(135deg,#8a5a3a 0%,#b8875e 35%,#d6b48e 60%,#9a6b47 100%)}
.hero-title{left:0;top:270px;width:1200px;text-align:center;color:var(--white);font:700 36px "Catamaran","Dosis",sans-serif}
.btn{border-radius:22px;font:600 12px "Dosis",sans-serif;text-transform:uppercase;display:flex;align-items:center;justify-content:center;letter-spacing:.3px}
.btn-fill{background:var(--orange);color:var(--white)}
.btn-line{border:1.5px solid var(--line);background:var(--white);color:var(--orange)}

.cat{top:497px;width:330px;height:300px;border-radius:10px;box-shadow:0 8px 18px rgba(0,0,0,.18);text-align:center;color:var(--white);font:700 25px "Dosis",sans-serif;padding-top:22px}
.cat .art{position:absolute;left:50px;top:75px;width:230px;height:180px;border-radius:4px}

/* product rows */
.sec-title{left:87px;font:600 25px "Dosis",sans-serif;color:#222}
.view-all{left:987px;width:124px;height:42px}
.arrow{width:46px;height:46px;border-radius:50%;display:flex;align-items:center;justify-content:center}
.arrow.grey{background:#e8e8e8}
.arrow.hot{background:var(--orange)}
.product{width:240px;text-align:center}
.product .cover{margin:0 auto;box-shadow:0 2px 6px rgba(0,0,0,.25)}
.price{font:500 23px "Dosis",sans-serif;color:var(--price)}
.pname{font:500 22px/1.2 "Dosis",sans-serif;color:#111}
.product .btn{margin:0 auto;width:122px;height:42px}

/* about */
.tab{top:2363px;width:140px;height:42px;font-size:11px}
.tab.current{background:#e0e0e0;border:none;color:var(--orange)}
.about-title{left:87px;top:2430px;width:480px;font:700 26px/1.35 "Catamaran","Dosis",sans-serif}
.about-text{left:87px;top:2507px;width:470px;font:600 15px/1.85 "Open Sans",sans-serif;color:#333}
.photo{left:584px;top:2360px;width:527px;height:308px;background:linear-gradient(160deg,#b9c7c9 0%,#8ea79a 45%,#6b8a4e 100%)}
.play{left:824px;top:2482px;width:64px;height:64px;border-radius:50%;background:rgba(255,255,255,.75)}

/* testimonials */
.testi{left:0;top:2782px;width:1200px;height:347px;background:var(--blue);color:var(--white);text-align:center}
.testi h2{font:700 25px "Dosis",sans-serif;margin-top:38px}
.quote{width:640px;margin:32px auto 0;font:600 18px/1.65 "Open Sans",sans-serif}
.stars{margin-top:14px;font-size:34px;line-height:1;color:#f5e21b;letter-spacing:6px}
.who{margin-top:14px;font:600 16px "Open Sans",sans-serif;color:#20394a}
.role{font:400 14px "Open Sans",sans-serif;color:#d8eef7;margin-top:2px}
.dots{display:flex;gap:12px;justify-content:center;margin-top:54px}
.dots span{width:10px;height:10px;border-radius:50%;background:#6db9dd}
.dots .on{background:#1f6e96}

/* footer */
.footer{left:0;top:3216px;width:1200px;height:300px;background:var(--footer);color:var(--white)}
.fcol{top:3262px;font:400 15px/34px "Open Sans",sans-serif}
.fcol h4{font:700 18px/24px "Dosis",sans-serif;margin-bottom:10px}
.newsletter{left:806px;top:3331px;width:305px;height:42px;border-radius:22px;background:#6f7c5f;display:flex;align-items:center;justify-content:space-between;font:400 13px "Open Sans",sans-serif;padding-left:22px;overflow:hidden}
.newsletter b{background:var(--white);color:#333;height:42px;width:104px;display:flex;align-items:center;justify-content:center;font-weight:600;border-radius:0 22px 22px 0}
.fsocial span{background:#7a8767;width:34px;height:34px}
.copy{left:0;top:3478px;width:1200px;text-align:center;font:400 13px "Open Sans",sans-serif;color:#dfe6d4}
</style>
</head>
<body>

<header>
  <div class="abs topbar"></div>
  <div class="abs logo">Pebble<br>Lantern<br>Kids</div>
  <div class="abs social" style="left:335px;top:31px"><span class="on"></span><span></span><span></span><span></span></div>
  <a class="abs pill" style="left:813px;top:28px;width:141px;height:42px">My Orders</a>
  <a class="abs pill" style="left:970px;top:28px;width:141px;height:42px">
    <svg width="26" height="20" viewBox="0 0 26 20"><path d="M1 2h4l3 11h13l3-8H7" fill="none" stroke="#d25028" stroke-width="2"/><circle cx="10" cy="17" r="2" fill="#d25028"/><circle cx="19" cy="17" r="2" fill="#d25028"/></svg>Cart</a>
  <div class="abs navbar"></div>
  <nav class="abs nav"><a class="active">Home</a><a>Products</a><a>About Us</a><a>Blog</a><a>Contact</a></nav>
  <div class="abs search">Search Here
    <svg width="24" height="24" viewBox="0 0 24 24"><circle cx="10" cy="10" r="7" fill="none" stroke="#fff" stroke-width="2.5"/><path d="M15 15l7 7" stroke="#fff" stroke-width="2.5"/></svg></div>
</header>

<section>
  <div class="abs hero" role="img" aria-label="Child drawing with coloured pencils on a wooden table"></div>
  <h1 class="abs hero-title">when children become the heroes of their own stories</h1>
  <a class="abs btn btn-fill" style="left:525px;top:356px;width:173px;height:42px">Learn More</a>

  <div class="abs cat" style="left:87px;background:var(--purple)">Popular Books
    <div class="art" role="img" aria-label="Stack of personalised storybook covers" style="background:linear-gradient(135deg,#f2c14e,#e25b8c 50%,#6fb3e0)"></div></div>
  <div class="abs cat" style="left:436px;background:var(--pink)">Popular Cartoon DVDs
    <div class="art" role="img" aria-label="Stack of cartoon DVD cases" style="background:linear-gradient(135deg,#f3d03c,#d8463a 50%,#3b7fd0)"></div></div>
  <div class="abs cat" style="left:783px;background:var(--green)">Popular Music CD's
    <div class="art" role="img" aria-label="Stack of children's music CD cases" style="background:linear-gradient(135deg,#5fb7ea,#e44a6a 50%,#f4d24a)"></div></div>
</section>

<!-- Personalised books -->
<section>
  <h2 class="abs sec-title" style="top:908px">Personalised Books</h2>
  <a class="abs btn btn-line view-all" style="top:905px">View All</a>
  <div class="abs arrow grey" style="left:64px;top:1046px"><svg width="12" height="16"><path d="M9 2L3 8l6 6" fill="none" stroke="#999" stroke-width="2"/></svg></div>
  <div class="abs arrow hot" style="left:1083px;top:1046px"><svg width="12" height="16"><path d="M3 2l6 6-6 6" fill="none" stroke="#fff" stroke-width="2"/></svg></div>

  <div class="abs product" style="left:91px;top:973px">
    <div class="cover" role="img" aria-label="Dinosaur storybook cover" style="width:140px;height:194px;background:linear-gradient(160deg,#f0c23a,#6fae3e 60%,#3f8ccf)"></div>
    <div class="price" style="margin-top:10px">€ 16,90</div><div class="pname">Dinosaure Dinosaure</div>
    <a class="btn btn-line" style="margin-top:8px">Add to Cart</a></div>
  <div class="abs product" style="left:351px;top:973px">
    <div class="cover" role="img" aria-label="Baby album cover in mint green" style="width:140px;height:194px;background:linear-gradient(180deg,#9ad8bf,#86cdb1)"></div>
    <div class="price" style="margin-top:10px">€ 19,90</div><div class="pname">FR Album de bébé</div>
    <a class="btn btn-line" style="margin-top:8px">Add to Cart</a></div>
  <div class="abs product" style="left:609px;top:973px">
    <div class="cover" role="img" aria-label="Dinosaur land storybook cover" style="width:140px;height:194px;background:linear-gradient(160deg,#f3c542,#79b443 60%,#4b8fcf)"></div>
    <div class="price" style="margin-top:10px">€ 24,60</div><div class="pname">Dinasour Land</div>
    <a class="btn btn-line" style="margin-top:8px">Add to Cart</a></div>
  <div class="abs product" style="left:867px;top:973px">
    <div class="cover" role="img" aria-label="Mysterious dragon storybook cover" style="width:140px;height:194px;background:linear-gradient(160deg,#9ec9ee,#8a6cc7 55%,#e6b64c)"></div>
    <div class="price" style="margin-top:10px">€ 15,80</div><div class="pname">FR Dragon mystérieux</div>
    <a class="btn btn-line" style="margin-top:8px">Add to Cart</a></div>
</section>

<!-- Music CDs -->
<section>
  <h2 class="abs sec-title" style="top:1381px">Music CDs</h2>
  <a class="abs btn btn-line view-all" style="top:1378px">View All</a>
  <div class="abs arrow grey" style="left:64px;top:1521px"><svg width="12" height="16"><path d="M9 2L3 8l6 6" fill="none" stroke="#999" stroke-width="2"/></svg></div>
  <div class="abs arrow grey" style="left:1083px;top:1521px"><svg width="12" height="16"><path d="M3 2l6 6-6 6" fill="none" stroke="#999" stroke-width="2"/></svg></div>

  <div class="abs product" style="left:91px;top:1472px">
    <div class="cover" role="img" aria-label="Animals music CD cover" style="width:150px;height:145px;background:linear-gradient(150deg,#f4e04a,#7cc444 55%,#3e9a3a)"></div>
    <div class="price" style="margin-top:14px">€ 19,90</div><div class="pname">Animals Are My Best<br>Friends</div>
    <a class="btn btn-fill" style="margin-top:6px">Add to Cart</a></div>
  <div class="abs product" style="left:351px;top:1472px">
    <div class="cover" role="img" aria-label="Animals love me music CD cover" style="width:150px;height:145px;background:linear-gradient(150deg,#f1a6c9,#f4e07a 55%,#9fd4ef)"></div>
    <div class="price" style="margin-top:14px">€ 19,90</div><div class="pname">Animals Love Me</div>
    <a class="btn btn-line" style="margin-top:8px">Add to Cart</a></div>
  <div class="abs product" style="left:609px;top:1472px">
    <div class="cover" role="img" aria-label="Purple Pal music CD cover" style="width:150px;height:145px;background:linear-gradient(150deg,#8ad0ef,#9b63c6 50%,#5cb84a)"></div>
    <div class="price" style="margin-top:14px">€ 19,60</div><div class="pname">Purple Pal</div>
    <a class="btn btn-line" style="margin-top:8px">Add to Cart</a></div>
  <div class="abs product" style="left:867px;top:1472px">
    <div class="cover" role="img" aria-label="Les Doudous rainbow music CD cover" style="width:150px;height:145px;background:linear-gradient(150deg,#7ec6ee,#f3a4c4 50%,#f6e25a)"></div>
    <div class="price" style="margin-top:14px">€ 19,80</div><div class="pname">Les Doudous</div>
    <a class="btn btn-line" style="margin-top:8px">Add to Cart</a></div>
</section>

<!-- Cartoon DVDs -->
<section>
  <h2 class="abs sec-title" style="top:1874px">Cartoon DVDs</h2>
  <a class="abs btn btn-line view-all" style="top:1870px">View All</a>
  <div class="abs arrow grey" style="left:64px;top:2010px"><svg width="12" height="16"><path d="M9 2L3 8l6 6" fill="none" stroke="#999" stroke-width="2"/></svg></div>
  <div class="abs arrow grey" style="left:1083px;top:2010px"><svg width="12" height="16"><path d="M3 2l6 6-6 6" fill="none" stroke="#999" stroke-width="2"/></svg></div>

  <div class="abs product" style="left:91px;top:1960px">
    <div class="cover" role="img" aria-label="Christmas adventure DVD case" style="width:90px;height:161px;background:linear-gradient(160deg,#2f7fd6,#d9412f 55%,#f2c23a)"></div>
    <div class="price" style="margin-top:12px">€ 27,90</div><div class="pname">My Christmas Adventure<br>DVD</div>
    <a class="btn btn-line" style="margin-top:6px">Add to Cart</a></div>
  <div class="abs product" style="left:351px;top:1960px">
    <div class="cover" role="img" aria-label="Snow White DVD case" style="width:90px;height:161px;background:linear-gradient(160deg,#f3d53c,#e6497a 55%,#3c7fd0)"></div>
    <div class="price" style="margin-top:12px">€ 27,90</div><div class="pname">Snow White</div>
    <a class="btn btn-line" style="margin-top:8px">Add to Cart</a></div>
  <div class="abs product" style="left:609px;top:1960px">
    <div class="cover" role="img" aria-label="Amazing dad DVD case" style="width:90px;height:161px;background:linear-gradient(160deg,#f2c43a,#d5402e 55%,#2f6fc4)"></div>
    <div class="price" style="margin-top:12px">€ 23,60</div><div class="pname">Amazing Dad</div>
    <a class="btn btn-line" style="margin-top:8px">Add to Cart</a></div>
  <div class="abs product" style="left:867px;top:1960px">
    <div class="cover" role="img" aria-label="Little Mermaid DVD case" style="width:90px;height:161px;background:linear-gradient(160deg,#f3d33c,#3fb0c9 55%,#2e6fc7)"></div>
    <div class="price" style="margin-top:12px">€ 27,80</div><div class="pname">Little Mermaid</div>
    <a class="btn btn-line" style="margin-top:8px">Add to Cart</a></div>
</section>

<!-- About -->
<section>
  <a class="abs btn btn-line tab current" style="left:87px">Watch a Video</a>
  <a class="abs btn btn-line tab" style="left:244px">Our Mission</a>
  <a class="abs btn btn-line tab" style="left:401px">Our Vision</a>
  <h2 class="abs about-title">Personalisation improves a child's learning ability and motivation</h2>
  <p class="abs about-text">Pebble Lantern Kids personalised books offers the possibility of sharing magical and unique moments which help the child become familiar with reading and inspire reading passion.&nbsp; Which is more special and magical than becoming the hero of your own story !</p>
  <a class="abs btn btn-fill" style="left:87px;top:2649px;width:124px;height:42px">Learn More</a>
  <div class="abs photo" role="img" aria-label="Two children in sun hats reading a book outdoors"></div>
  <div class="abs play"><svg width="64" height="64"><path d="M26 20l20 12-20 12z" fill="#fff"/></svg></div>
</section>

<!-- Testimonials -->
<section class="abs testi">
  <h2>What Our Customers Are Saying</h2>
  <p class="quote">“ Donec mi sapien, congue eu massa vel, elementum volutpat justo.ullamcorper diam gravida Proin luctus eleifend erat non luctus.”</p>
  <div class="stars">★★★★★</div>
  <div class="who">Mara Ellison</div>
  <div class="role">Customer</div>
  <div class="dots"><span class="on"></span><span></span><span></span></div>
</section>

<!-- Footer -->
<footer>
  <div class="abs footer"></div>
  <div class="abs logo" style="top:3254px;left:82px">Pebble<br>Lantern<br>Kids</div>
  <div class="abs fcol" style="left:244px"><h4>Support</h4>Order samples<br>About Us<br>Contact Us<br>Recruitment<br>Sucess Stories</div>
  <div class="abs fcol" style="left:420px"><h4>Collections</h4>Our Collections<br>Personalised books<br>Personalised music albums<br>Personalised DVD cartoon<br>Personalised school books</div>
  <div class="abs fcol" style="left:647px"><h4>Packs</h4>Discovery pack<br>Gold pack<br>Platinium pack</div>
  <div class="abs fcol" style="left:806px"><h4>Subscribe To Our Newsletter</h4>Get Latest Discount Offer Updates</div>
  <div class="abs newsletter">Email Address<b>Subscribe</b></div>
  <div class="abs social fsocial" style="left:806px;top:3407px"><span></span><span></span><span></span><span></span></div>
  <div class="abs copy">©Pebblelanternkids. All Rights Reserved</div>
</footer>

</body>
</html>
```